Baby acupressure app for parents

We need an app for parents that teaches parents how to help them relieve their baby's imbalances (stomach ache, trouble sleeping etc.)

Please see the attached document (with info) and wireframes.

This project is urgent so please only participate if you're able to finish all screens within a few days after the contest is over.

Target Market(s)

Baby moms (20-40 years of age)

Industry/Entity Type

Baby Care

Colors
886aae
b768aa
e667a6
f68d4d
faa54b
fac994
f9ba93
f59195
fee18a

Requirements
Must have
• A high quality design that is both modern and very sleek and stylish.
Nice to have
• Simple animations to make the app "feel" like it's extreme high quality and make the user want to use it again and again
Should not have
• Sandwich menus

```html
<!DOCTYPE html>
<html lang="en">
<head>
<meta charset="UTF-8">
<title>Rolig og Varm – Welcome</title>
<link rel="stylesheet" href="https://fonts.googleapis.com/css2?family=Figtree:wght@600;700;800;900&display=swap">
<style>
  :root {
    --purple-deep: #5d4a7a;
    --purple-mid: #7d67a0;
    --purple-soft: #8e77b0;
    --white: #ffffff;
    --lavender-text: #e6ddf0;
    --orange: #f9a24a;
    --disclaimer: rgba(225, 218, 232, 0.82);
  }
  * { margin: 0; padding: 0; box-sizing: border-box; }
  html, body { width: 675px; height: 1200px; overflow: hidden; background: var(--purple-deep); }
  .welcome-screen {
    position: relative;
    width: 675px;
    height: 1200px;
    overflow: hidden;
    font-family: "Figtree", "Helvetica Neue", Arial, sans-serif;
    color: var(--white);
    text-align: center;
  }
  .hero-photo {
    position: absolute;
    inset: 0;
    background:
      radial-gradient(ellipse 60% 45% at 62% 38%, var(--purple-soft) 0%, transparent 70%),
      radial-gradient(ellipse 55% 40% at 35% 78%, #6e5b85 0%, transparent 75%),
      linear-gradient(180deg, var(--purple-mid) 0%, #6f5a90 45%, var(--purple-deep) 100%);
  }
  .brand-mark {
    position: absolute;
    left: 50%;
    top: 224px;
    width: 200px;
    height: 200px;
    transform: translateX(-50%);
  }
  .app-name {
    position: absolute;
    top: 506px;
    width: 100%;
    font-size: 32px;
    font-weight: 700;
    letter-spacing: 0.2px;
  }
  .tagline {
    position: absolute;
    top: 571px;
    width: 100%;
    font-size: 23px;
    font-weight: 700;
    color: var(--lavender-text);
  }
  .begin-button {
    position: absolute;
    top: 762px;
    left: 0;
    width: 100%;
    font-size: 142px;
    font-weight: 800;
    line-height: 1;
    color: var(--orange);
    letter-spacing: -1px;
  }
  .disclaimer {
    position: absolute;
    top: 1040px;
    width: 100%;
    font-size: 23px;
    font-weight: 700;
    line-height: 34px;
    color: var(--disclaimer);
  }
</style>
</head>
<body>
<main class="welcome-screen">
  <div class="hero-photo" role="img" aria-label="Photo of a mother holding her baby close, with a purple overlay"></div>

  <svg class="brand-mark" viewBox="0 0 200 200" aria-hidden="true">
    <circle cx="100" cy="100" r="96" fill="var(--white)"/>
  </svg>

  <h1 class="app-name">Rolig og Varm</h1>
  <p class="tagline">Help relieve your child balance</p>

  <div class="begin-button">BEGIN</div>

  <p class="disclaimer">Always consult a physician if you suspect your child<br>is in need of health care. See FAQ for more info.</p>
</main>
</body>
</html>
```